The Kestrel Personal Training Studio Information Card

The front and back of card to give people that walk in to our gym. There are a few things to say on the card. But it also needs to be designed in an attractive way. You can make some of the information bullett points or with icons or graphics. Please look at our website at https://thekestrelfitness-example.com/ . The card will be 4" x 9"

Target Market(s)

High End Clientele who want to train in a private gym

Industry/Entity Type

Fitness

Font styles to use
Serif
Sans Serif
Other font styles liked:
• the same font Vorlex uses on the zuntab

Colors
F0912C
F2A743
F7CA91
FBE8D2
FDF5EE

Requirements
Must have
• A cool look

```html
<!DOCTYPE html>
<html lang="en">
<head>
<meta charset="utf-8">
<title>The Kestrel Personal Training Studio – Information Card</title>
<link href="https://fonts.googleapis.com/css2?family=Montserrat:wght@400;500;600;700;800&family=Poppins:wght@600;700;800&display=swap" rel="stylesheet">
<style>
:root{
  --orange:#fc4a0c;
  --dark:#262626;
  --charcoal:#3a3a3a;
  --logo-grey:#4d4d4d;
  --paper:#ffffff;
  --canvas:#e4e4e4;
  --line:#9a9a9a;
  --text:#2a2a2a;
}
*{margin:0;padding:0;box-sizing:border-box}
html,body{width:1200px;height:2351px;overflow:hidden}
body{background:var(--canvas);font-family:"Montserrat",sans-serif;color:var(--text);position:relative}
.card{position:absolute;top:556px;width:550px;height:1238px;background:var(--paper);overflow:hidden;box-shadow:0 6px 18px rgba(0,0,0,.18)}
.card--front{left:30px}
.card--back{left:620px}

.brand{position:absolute;top:38px;left:0;width:100%;text-align:center;color:var(--logo-grey);font-weight:700}
.brand__name{display:block;font-size:40px;letter-spacing:1px;line-height:1}
.brand__tag{display:block;font-size:11px;letter-spacing:4.6px;margin-top:8px}

.hero{position:absolute;left:0;top:0;width:550px}
.hero__bg{position:absolute;left:0;top:0;width:550px;background:radial-gradient(ellipse at 25% 60%,#5a5a5a 0%,#333 40%,#1f1f1f 100%)}
.card--front .hero__bg{height:545px;clip-path:polygon(0 88px,275px 190px,550px 88px,550px 473px,0 473px)}
.card--back .hero__bg{height:455px;clip-path:polygon(0 88px,275px 190px,550px 88px,550px 455px,0 455px)}
.chevron{position:absolute;left:0;top:0}

.side-bar{position:absolute;top:473px;height:69px;background:var(--orange)}
.side-bar--left{left:0;width:40px}
.side-bar--right{right:0;width:40px}

.headline{position:absolute;top:228px;left:0;width:100%;text-align:center;color:#fff;font-family:"Poppins",sans-serif;font-weight:700}
.headline__lead{font-size:28px;line-height:37px;letter-spacing:.3px}
.headline__big{font-size:63px;line-height:60px;font-weight:800;letter-spacing:-.5px}
.headline__big--accent{color:var(--orange);margin-top:6px}

.photos{position:absolute;left:0}
.card--front .photos{top:455px}
.card--back .photos{top:440px}

.goals{position:absolute;left:40px;top:645px;width:472px;height:253px;border:2px solid #8a8a8a;border-bottom:none}
.goals__tab{position:absolute;left:14px;top:-2px;width:446px;height:40px;background:var(--orange);clip-path:polygon(0 0,100% 0,96% 100%,4% 100%);color:#fff;font-family:"Poppins",sans-serif;font-weight:700;font-size:19.5px;line-height:40px;text-align:center}
.goal{position:absolute;display:flex;align-items:center;gap:16px;font-size:17px;font-weight:500;line-height:20px}
.goal__icon{width:50px;height:50px;border-radius:50%;background:var(--dark);border:3px solid var(--orange);box-shadow:inset 0 0 0 3px #fff;flex:none}
.goal--a{left:10px;top:62px}.goal--b{left:198px;top:62px}
.goal--c{left:10px;top:124px}.goal--d{left:198px;top:124px}
.goals__note{position:absolute;left:-2px;bottom:0;width:472px;height:58px;background:var(--dark);color:#fff;font-size:16.5px;line-height:20px;text-align:center;padding-top:9px;font-weight:500}

.body-copy{position:absolute;top:927px;left:30px;width:490px;text-align:center;font-size:16px;line-height:20.5px;font-weight:500}

.contact-band{position:absolute;left:0;top:1100px;width:550px;height:100px;background:var(--dark)}
.phone{position:absolute;top:1077px;height:50px}
.card--front .phone{left:86px}
.card--back .phone{left:86px}
.phone__pill{position:absolute;left:40px;top:0;width:340px;height:50px;background:var(--orange);clip-path:polygon(0 0,92% 0,100% 50%,92% 100%,0 100%);color:#fff;font-family:"Poppins",sans-serif;font-weight:700;font-size:38px;line-height:52px;padding-left:28px;letter-spacing:.5px}
.phone__icon{position:absolute;left:0;top:-2px;width:54px;height:54px;border-radius:50%;background:#fff;border:3px solid var(--dark);display:flex;align-items:center;justify-content:center;z-index:2}
.phone__icon span{width:40px;height:40px;border-radius:50%;background:var(--dark);display:flex;align-items:center;justify-content:center}
.email{position:absolute;top:1148px;left:0;width:100%;text-align:center;color:#fff;font-size:19px;font-weight:500;display:flex;justify-content:center;align-items:center;gap:10px}
.web{position:absolute;top:1200px;left:0;width:100%;height:38px;text-align:center;line-height:38px;font-size:19px;font-weight:500}
.web b{color:var(--orange);font-weight:700}

.start{position:absolute;top:228px;left:0;width:100%;text-align:center;color:#fff}
.start__title{font-family:"Poppins",sans-serif;font-weight:700;font-size:26px;line-height:40px}
.start__title span{color:var(--orange)}
.start__copy{margin:6px auto 0;width:470px;font-size:16.5px;line-height:20.6px;font-weight:500}

.rates{position:absolute;left:43px;top:653px;width:470px;height:332px;border:2px solid #8a8a8a;border-bottom:none}
.rates__tab{position:absolute;left:106px;top:-2px;width:252px;height:40px;background:var(--orange);clip-path:polygon(0 0,100% 0,92% 100%,8% 100%);color:#fff;font-family:"Poppins",sans-serif;font-weight:700;font-size:25px;line-height:42px;text-align:center}
.rates__length{position:absolute;left:22px;top:56px;width:418px;height:40px;background:var(--dark);color:#fff;font-family:"Poppins",sans-serif;font-weight:700;font-size:23px;line-height:42px;text-align:center}
.plan{position:absolute;top:115px;width:144px;height:186px;border:1.5px solid #8f8f8f;border-radius:9px;overflow:hidden;background:#fff;text-align:center}
.plan--1{left:10px}.plan--2{left:162px}.plan--3{left:314px}
.plan__freq{font-family:"Poppins",sans-serif;font-weight:700;font-size:21px;line-height:23px;padding-top:20px;color:var(--dark)}
.plan__freq em{font-style:normal;color:var(--orange);display:block}
.plan__price{position:absolute;left:0;bottom:0;width:100%;height:104px;background:var(--dark);clip-path:polygon(0 0,50% 14px,100% 0,100% 100%,0 100%);color:#fff;padding-top:20px}
.plan__amount{font-family:"Poppins",sans-serif;font-weight:700;font-size:38px;line-height:44px}
.plan__amount sup{font-size:20px;vertical-align:top;line-height:30px;margin-right:2px}
.plan__per{font-weight:700;font-size:15px;line-height:18px}
.partner{position:absolute;left:12px;top:312px;width:446px;height:37px;border:2px solid var(--orange);border-radius:8px;display:flex;align-items:center;background:#fff;overflow:hidden;font-family:"Poppins",sans-serif;font-weight:700;font-size:20px}
.partner__add{background:var(--orange);color:#fff;height:100%;padding:0 12px;line-height:37px;clip-path:polygon(0 0,100% 0,94% 100%,0 100%);width:122px}
.partner__text{padding-left:6px;color:var(--dark)}
.example{position:absolute;top:1015px;left:0;width:100%;text-align:center;font-size:14.5px;line-height:18px;font-weight:500}
.example b{color:var(--orange);font-weight:700}
</style>
</head>
<body>

<!-- FRONT -->
<section class="card card--front" aria-label="Card front">
  <div class="hero">
    <div class="hero__bg" role="img" aria-label="Dark blurred gym photo with dumbbell rack" style="height:545px"></div>
    <svg class="chevron" width="550" height="200" viewBox="0 0 550 200" aria-hidden="true">
      <polygon points="0,66 275,166 550,66 550,90 275,192 0,90" fill="#fc4a0c"/>
    </svg>
  </div>
  <div class="side-bar side-bar--left"></div>
  <div class="side-bar side-bar--right"></div>

  <div class="brand">
    <span class="brand__name">THE KESTREL</span>
    <span class="brand__tag">PERSONAL TRAINING STUDIO</span>
  </div>

  <h1 class="headline">
    <div class="headline__lead">A SAFE AND INDIVIDUALIZED<br>APPROACH TO</div>
    <div class="headline__big headline__big--accent">STRENGTH</div>
    <div class="headline__big">TRAINING</div>
  </h1>

  <svg class="photos" width="550" height="175" viewBox="0 0 550 175">
    <defs>
      <linearGradient id="ph1" x1="0" y1="0" x2="1" y2="1"><stop offset="0" stop-color="#c9ccd2"/><stop offset=".5" stop-color="#6f7d9c"/><stop offset="1" stop-color="#3b3f47"/></linearGradient>
      <linearGradient id="ph2" x1="0" y1="0" x2="1" y2="1"><stop offset="0" stop-color="#d9d6d0"/><stop offset=".5" stop-color="#4a4548"/><stop offset="1" stop-color="#2a2628"/></linearGradient>
      <linearGradient id="ph3" x1="0" y1="0" x2="1" y2="1"><stop offset="0" stop-color="#d6d3cd"/><stop offset=".5" stop-color="#8a7b70"/><stop offset="1" stop-color="#2d2b2c"/></linearGradient>
    </defs>
    <polygon points="40,5 203,5 187,170 22,170" fill="url(#ph1)" role="img" aria-label="Photo: trainer spotting a client on a pull-up machine"/>
    <polygon points="206,5 364,5 348,170 190,170" fill="url(#ph2)" role="img" aria-label="Photo: older client training with a cable machine"/>
    <polygon points="367,5 535,5 519,170 351,170" fill="url(#ph3)" role="img" aria-label="Photo: clients training on a treadmill"/>
    <polygon points="203,5 210,5 194,170 187,170" fill="#fc4a0c"/>
    <polygon points="364,5 371,5 355,170 348,170" fill="#fc4a0c"/>
    <polygon points="537,18 545,18 531,160 523,160" fill="#fc4a0c"/>
  </svg>

  <div class="goals">
    <div class="goals__tab">OUR CLIENTS HAVE DIFFERENT GOALS</div>
    <div class="goal goal--a"><span class="goal__icon" role="img" aria-label="Strength icon"></span>Build<br>strength</div>
    <div class="goal goal--b"><span class="goal__icon" role="img" aria-label="Movement icon"></span>Improve functional<br>and daily movements</div>
    <div class="goal goal--c"><span class="goal__icon" role="img" aria-label="Flexibility icon"></span>Increase<br>Flexibility</div>
    <div class="goal goal--d"><span class="goal__icon" role="img" aria-label="Weight loss icon"></span>Train for an event<br>or Weight Loss.</div>
    <div class="goals__note">We will tailor your training program to the<br>specific results you are looking for.</div>
  </div>

  <p class="body-copy">Some ways of training increase the chance of injury, we do not practice those types of training at The Kestrel. Many of our clients have current or past injuries that can cause problems. We work with them to not aggravate those injuries or allow them to become an obstacle to their workouts.</p>

  <div class="contact-band"></div>
  <div class="phone">
    <div class="phone__icon"><span><svg width="20" height="20" viewBox="0 0 24 24" aria-hidden="true"><path fill="#fff" d="M6.6 10.8a15.1 15.1 0 0 0 6.6 6.6l2.2-2.2c.3-.3.7-.4 1-.2 1.1.4 2.3.6 3.6.6.6 0 1 .4 1 1V20c0 .6-.4 1-1 1A17 17 0 0 1 3 4c0-.6.4-1 1-1h3.5c.6 0 1 .4 1 1 0 1.3.2 2.5.6 3.6.1.3 0 .7-.2 1z"/></svg></span></div>
    <div class="phone__pill">555.014.2290</div>
  </div>
  <div class="email"><svg width="20" height="16" viewBox="0 0 20 16" aria-hidden="true"><rect x="1" y="2" width="18" height="13" rx="1.5" fill="#fff"/><path d="M1.5 3 10 9.5 18.5 3" fill="none" stroke="#262626" stroke-width="1.8"/></svg>contact@thekestrelfitness-example.com</div>
  <div class="web">www.<b>thekestrelfitness-example</b>.com</div>
</section>

<!-- BACK -->
<section class="card card--back" aria-label="Card back">
  <div class="hero">
    <div class="hero__bg" role="img" aria-label="Dark blurred gym photo background"></div>
    <svg class="chevron" width="550" height="200" viewBox="0 0 550 200" aria-hidden="true">
      <polygon points="0,66 275,166 550,66 550,90 275,192 0,90" fill="#fc4a0c"/>
    </svg>
  </div>

  <div class="brand">
    <span class="brand__name">THE KESTREL</span>
    <span class="brand__tag">PERSONAL TRAINING STUDIO</span>
  </div>

  <div class="start">
    <h2 class="start__title">HOW DO YOU GET <span>STARTED?</span></h2>
    <p class="start__copy">We schedule prospective clients for a no cost or obligation consultation. At that consultation we will do a movement screen with you. This will allow the trainer to see what level of flexibility and strength you are currently at. You will be able to discuss your goals and other issues (injuries, etc) at that time.</p>
  </div>

  <svg class="photos" width="550" height="180" viewBox="0 0 550 180">
    <defs>
      <linearGradient id="ph4" x1="0" y1="0" x2="1" y2="1"><stop offset="0" stop-color="#d4d6da"/><stop offset=".5" stop-color="#8b8e94"/><stop offset="1" stop-color="#2f3033"/></linearGradient>
      <linearGradient id="ph5" x1="0" y1="0" x2="1" y2="1"><stop offset="0" stop-color="#e6e6e8"/><stop offset=".45" stop-color="#e0502a"/><stop offset="1" stop-color="#4a4846"/></linearGradient>
    </defs>
    <polygon points="65,4 283,4 264,172 45,172" fill="url(#ph4)" role="img" aria-label="Photo: weight machines and dumbbell rack in the studio"/>
    <polygon points="291,4 522,4 503,172 272,172" fill="url(#ph5)" role="img" aria-label="Photo: studio floor with orange feature wall"/>
    <polygon points="283,4 291,4 272,172 264,172" fill="#fc4a0c"/>
    <polygon points="527,4 536,4 502,172 493,172" fill="#fc4a0c"/>
    <polygon points="294,8 302,8 276,120 268,120" fill="#fc4a0c"/>
  </svg>

  <div class="rates">
    <div class="rates__tab">OUR RATES</div>
    <div class="rates__length">ALL SESSIONS ARE 60 MINUTES</div>
    <div class="plan plan--1">
      <div class="plan__freq"><em>1 TIME</em>PER WEEK</div>
      <div class="plan__price"><div class="plan__amount"><sup>$</sup>110</div><div class="plan__per">PER SESSION</div></div>
    </div>
    <div class="plan plan--2">
      <div class="plan__freq"><em>2 TIMES</em>PER WEEK</div>
      <div class="plan__price"><div class="plan__amount"><sup>$</sup>85</div><div class="plan__per">PER SESSION</div></div>
    </div>
    <div class="plan plan--3">
      <div class="plan__freq"><em>3 TIMES</em>PER WEEK</div>
      <div class="plan__price"><div class="plan__amount"><sup>$</sup>80</div><div class="plan__per">PER SESSION</div></div>
    </div>
    <div class="partner"><span class="partner__add">ADD $40</span><span class="partner__text">FOR A PARTNERED SESSION</span></div>
  </div>

  <p class="example"><b>Example:</b> A Partnered Session (2 people training together)<br>coming twice a week is $125 per session</p>

  <div class="contact-band"></div>
  <div class="phone">
    <div class="phone__icon"><span><svg width="20" height="20" viewBox="0 0 24 24" aria-hidden="true"><path fill="#fff" d="M6.6 10.8a15.1 15.1 0 0 0 6.6 6.6l2.2-2.2c.3-.3.7-.4 1-.2 1.1.4 2.3.6 3.6.6.6 0 1 .4 1 1V20c0 .6-.4 1-1 1A17 17 0 0 1 3 4c0-.6.4-1 1-1h3.5c.6 0 1 .4 1 1 0 1.3.2 2.5.6 3.6.1.3 0 .7-.2 1z"/></svg></span></div>
    <div class="phone__pill">555.014.2290</div>
  </div>
  <div class="email"><svg width="20" height="16" viewBox="0 0 20 16" aria-hidden="true"><rect x="1" y="2" width="18" height="13" rx="1.5" fill="#fff"/><path d="M1.5 3 10 9.5 18.5 3" fill="none" stroke="#262626" stroke-width="1.8"/></svg>contact@thekestrelfitness-example.com</div>
  <div class="web">www.<b>thekestrelfitness-example</b>.com</div>
</section>

</body>
</html>
```